Cloud-based Health 2.0 Web Site

We need the overall look and feel for a new cloud-based Health 2.0 web site where health professionals can manage and interact with their patients/clients.

The plan is to generate a landing page that can grab the attention of health professionals (doctors, nurses, personal trainers, etc...). This page should have an attractive "Sign Up for Free" or similar button/message, as well as a login section for users already registered. We currently have a view on having a number of messages displayed, either as a slider or as separate areas on the page (decision is up for grabs).

Secondly, we need a standard "framework" for all the other pages which will be accessible once the user has authenticated with a clean, airy and spacious feel. This will provide styling for standard elements (input boxes, checkboxes, etc...) as well as a given layout, possibly 3 columns (fixed-fluid-fixed) although we leave this to the designer's choice.

We want to stress the importance of the Cloud, as well as make users feel like "this is the place to be if you're a modern, tech savvy health professional". Also of high importance is to show that this is a secure place, where data is accessible from anywhere yet also highly protected.

This project is going to provide long-term work for the winner and possibly those we consider close runner ups, so if you guys are interested in grabbing our attention so you can become our designer of choice, this is your chance!

Standard pages we are looking to receive after the selection process:

* Landing page
* Health Professional Profile Page (personal details, professional details, photo...)
* Patient list / Patient Management page
* Patient profile (details, health details...)
* Generic "item" management page (item refers to documents, images, contacts, etc...)

The logo for the site/product is also up for grabs, and a bonus payment can be given if you provide one that both matches the style of the site whilst being one that could be reused for mobile app icons, etc...

The site name is "vornatik" (all lower-case) for those of you wanting to work on the logo part. As I said before, the logo should contain a component that could be use as the recognisable icon in a mobile phone app. Something that can be easily identified in both the site and the app that connects them together.

vornatik is made up of two parts (vorn + atik), and you might want to consider differentiating them by the use of colour, fonts or however you think appropriate.

New sample screen-shots of the existing functionality have been uploaded to help you mock up some screens.

PLEASE NOTE: This are to be used for content/widget design only! The layout of how these are represented, e.g. accordion, slider, tree, list... is entirely up to you! Don't guide your layout based on these screen-shots, unless you think they are the way to go, of course. 

We want your creative input, so please innovate! :)

Thanks!

Target Market(s)

Health Professionals

Industry/Entity Type

Health

Requirements
Must have
• * A landing page that grabs the users attention but is "different" from the rest of pages (although within the same design/style parameters)

* A generic page framework for the rest of the pages (style guide)
Nice to have
• A modern and clean logo to go with the site. If the logo is selected, this can result in a bonus payment to be decided.

```html
<!DOCTYPE html>
<html lang="en">
<head>
<meta charset="utf-8">
<title>meridel – health 2.0 in the cloud</title>
<link href="https://fonts.googleapis.com/css2?family=Arimo:wght@400;700&display=swap" rel="stylesheet">
<style>
  :root{
    --page:#ffffff;
    --topbar:#dedede;
    --account:#d9d9d9;
    --navy:#1b2d6b;
    --hero:#5b86e6;
    --hero-panel:#7096e8;
    --band:#2a66d2;
    --orange:#f7931e;
    --orange-dark:#e67e10;
    --heading:#f5841f;
    --text:#1a1a1a;
    --footer:#2966d3;
    --copy:#1f5ccf;
  }
  *{margin:0;padding:0;box-sizing:border-box}
  html,body{width:1105px;height:1200px;overflow:hidden;background:var(--page)}
  body{position:relative;font-family:"Arimo",Arial,sans-serif;color:var(--text)}
  .abs{position:absolute}

  .top-strip{left:0;top:0;width:1105px;height:6px;background:var(--topbar)}
  .account{left:847px;top:6px;width:224px;height:38px;background:var(--account);display:flex}
  .account a{flex:1;display:flex;align-items:center;justify-content:center;gap:8px;font-size:14px;color:#111;text-decoration:none}
  .account a + a{border-left:3px solid #fff}

  .brand{left:76px;top:34px;display:flex;align-items:center;gap:10px;font-size:46px;color:var(--navy);letter-spacing:1px}
  .brand-dot{width:40px;height:40px;border-radius:50%;background:#2f8ff0}

  .hero-band{left:0;top:171px;width:1105px;height:335px;background:var(--hero)}
  .hero-panel{left:641px;top:171px;width:464px;height:335px;background:linear-gradient(135deg,#7d9fea 0%,var(--hero-panel) 60%,#5d88e4 100%)}
  .hero-photo{left:37px;top:121px;width:604px;height:385px;border-radius:10px 10px 0 0;
    background:linear-gradient(135deg,#c9a879 0%,#e8d6ad 55%,#b88a68 100%)}

  .tabs .tab{position:absolute;display:flex;align-items:center;justify-content:center;font-size:19px;color:#fff;border-radius:10px 10px 0 0;background:linear-gradient(#3aa2f7,#1f7fe4)}
  .tab.home{left:649px;top:120px;width:141px;height:51px;color:#111;background:linear-gradient(#fba040,var(--orange-dark))}
  .tab.about{left:792px;top:130px;width:133px;height:41px}
  .tab.contact{left:928px;top:130px;width:141px;height:41px}

  .hero-copy{left:671px;top:230px;color:#fff;line-height:1.15}
  .hero-copy .small{font-size:29px}
  .hero-copy .big{font-size:45px;line-height:56px}
  .hero-next{left:1043px;top:268px}

  .intro{left:0;top:506px;width:1105px;height:114px;background:var(--band);border-bottom:2px solid #9bb8ee}
  .intro p{position:absolute;left:63px;top:20px;width:935px;font-size:14px;line-height:23px;color:#fff}
  .intro .more{position:absolute;left:934px;top:89px;font-size:13.5px;color:#111}

  .feature{position:absolute;top:646px;width:309px}
  .feature .img{height:155px;border-radius:12px}
  .feature h2{font-weight:400;font-size:25px;color:var(--heading);margin:12px 0 0 5px}
  .feature p{font-size:13.4px;line-height:21px;margin:6px 0 0 7px;letter-spacing:.2px;width:290px}
  .f2 p{width:282px}
  .f1{left:59px}.f2{left:397px}.f3{left:733px}
  .f1 .img{background:linear-gradient(135deg,#8fb0d2 0%,#4a7fae 100%)}
  .f2 .img{background:linear-gradient(135deg,#1c2440 0%,#07102a 100%)}
  .f3 .img{background:linear-gradient(135deg,#a9c8ee 0%,#2f7ede 100%)}
  .btn{position:absolute;top:1031px;width:103px;height:27px;border-radius:14px;background:linear-gradient(#6cbcfa,#1f86ec);font-size:13.5px;color:#111;display:flex;align-items:center;justify-content:center}

  .footer{left:0;top:1104px;width:1105px;height:65px;background:var(--footer)}
  .footer nav a{position:absolute;top:25px;font-size:13px;color:#fff;text-decoration:none}
  .social{position:absolute;left:926px;top:21px;display:flex;gap:8px}
  .social span{width:22px;height:22px;border-radius:3px}
  .copyright{left:0;top:1180px;width:1105px;text-align:center;font-size:12.5px;color:var(--copy)}
</style>
</head>
<body>
  <div class="abs top-strip"></div>

  <div class="abs account">
    <a href="#">
      <svg width="18" height="18" viewBox="0 0 18 18"><circle cx="9" cy="5" r="4" fill="#8a6d3b"/><rect x="3" y="10" width="12" height="7" rx="3" fill="#c9a25a"/></svg>
      Login</a>
    <a href="#">
      <svg width="20" height="18" viewBox="0 0 20 18"><circle cx="8" cy="5" r="4" fill="#444"/><rect x="1" y="10" width="13" height="7" rx="3" fill="#555"/><path d="M13 15l6-6" stroke="#d22" stroke-width="2.5"/></svg>
      Sign up</a>
  </div>

  <div class="abs brand"><span class="brand-dot"></span>meridel</div>

  <div class="abs hero-band"></div>
  <div class="abs hero-panel"></div>
  <div class="abs hero-photo" role="img" aria-label="Photo of a doctor listening to a young patient's heartbeat with a stethoscope"></div>

  <nav class="tabs">
    <a class="tab home">Home</a>
    <a class="tab about">About</a>
    <a class="tab contact">Contact</a>
  </nav>

  <div class="abs hero-copy">
    <div class="small">the ultimate platform for</div>
    <div class="big" style="margin-top:6px">health care<br>professionals<br>and patients</div>
    <div class="small">to meet in the cloud.</div>
  </div>
  <svg class="abs hero-next" width="24" height="146" viewBox="0 0 24 146"><path d="M0 0L24 68L0 146Z" fill="#ffffff" opacity=".35"/></svg>

  <section class="abs intro">
    <p>Meridel is an Early Access Preview to some of vornatik's health 2.0 cloud-based engine.If you have arrived here through one of &nbsp;our invitation emails, please go ahead and logon to the system by using the username and password that were provided to you &nbsp;on your welcome email. If you have landed on this page by mistake, there is no problem, feel free to browse around and learn more about meridel.</p>
    <span class="more">Read More</span>
  </section>

  <article class="feature f1">
    <div class="img" role="img" aria-label="Photo of a woman running along a beach"></div>
    <h2>Health 2.0</h2>
    <p>Applying new technologies to solve the problem of health management has been the dream of many for a long time. With today's technology we are closer than ever to achieve this dream, and vornatik represents a col-lection of unique technologies and ideas that will revolutionaise the way people think, care for and manage health.</p>
  </article>
  <article class="feature f2">
    <div class="img" role="img" aria-label="Illustration of a locked document folder with a key"></div>
    <h2>Security</h2>
    <p>When online, nothing is more important that security, especially when dealing with health information. vornatik is designed from the ground up to be secure and to protect data in a number of different ways to ensure both strong access and data records anonymity.</p>
  </article>
  <article class="feature f3">
    <div class="img" role="img" aria-label="Photo of a man touching a transparent cloud screen against a blue sky"></div>
    <h2>Cloud-based</h2>
    <p>meridel represents a small part of the advanced health 2.0 engine that is vornatik and therefore it is designed and built for the Cloud. Data is safely stored in the cloud and users can accessed it from anywhere as long as they are authenticated and connected over a secure channel.</p>
  </article>

  <a class="btn" style="left:148px">Read More</a>
  <a class="btn" style="left:508px">Read More</a>
  <a class="btn" style="left:851px">Read More</a>

  <footer class="abs footer">
    <nav>
      <a href="#" style="left:66px">Home</a>
      <a href="#" style="left:153px">About</a>
      <a href="#" style="left:241px">Contact</a>
    </nav>
    <div class="social" aria-label="Social links">
      <span style="background:#222"></span>
      <span style="background:#4fb6ea"></span>
      <span style="background:#3b5fa8"></span>
      <span style="background:#f07a1e"></span>
    </div>
  </footer>

  <div class="abs copyright">© 2012 - corvane ltd</div>
</body>
</html>
```